The Bright Clinic Growth Hour

I need a podcast artwork designed for me for a new podcast I am launching
Target Market(s)
Chiropractors
Industry/Entity Type
Chiropractor
Requirements
Must have
- This image and the title of the show

```html
<!DOCTYPE html>
<html lang="en">
<head>
<meta charset="utf-8">
<title>The Bright Clinic Growth Hour – Podcast Artwork</title>
<link rel="stylesheet" href="https://fonts.googleapis.com/css2?family=Anton&family=Archivo+Black&family=Lobster&family=Oswald:wght@700&display=swap">
<style>
  :root {
    --page: #ffffff;
    --stone-light: #c89a72;
    --stone-mid: #8a5a3c;
    --stone-dark: #3b2a22;
    --title-red: #e0140e;
    --title-red-dark: #6a0704;
    --title-white: #ffffff;
    --title-cyan: #1e8fc0;
    --orange-top: #ffd23a;
    --orange-bottom: #e0300c;
    --name-top: #fff6b0;
    --name-bottom: #e8a400;
    --ink: #111111;
  }
  html, body {
    margin: 0;
    width: 1200px;
    height: 758px;
    overflow: hidden;
    background: var(--page);
  }
  .sheet { position: relative; width: 1200px; height: 758px; }

  .cover-slot { position: absolute; overflow: hidden; }
  .cover-slot--large  { left: 23px;  top: 23px;  width: 711px; height: 711px; }
  .cover-slot--medium { left: 777px; top: 61px;  width: 402px; height: 401px; }
  .cover-slot--small  { left: 872px; top: 477px; width: 213px; height: 213px; }

  .cover {
    position: absolute; left: 0; top: 0;
    width: 711px; height: 711px;
    transform-origin: 0 0;
    overflow: hidden;
    background: var(--stone-dark);
  }
  .cover-slot--medium .cover { transform: scale(0.5654); }
  .cover-slot--small  .cover { transform: scale(0.2996); }

  .cover__photo {
    position: absolute; inset: 0;
    background: radial-gradient(ellipse at 70% 40%, var(--stone-light) 0%, var(--stone-mid) 50%, var(--stone-dark) 100%);
  }
  .cover__layer { position: absolute; inset: 0; width: 711px; height: 711px; }

  .title { position: absolute; left: 0; top: 0; width: 711px; height: 711px; }
  .title__line { position: absolute; margin: 0; white-space: nowrap; line-height: 1; }

  .title__the {
    left: 40px; top: 92px;
    font: 84px "Lobster", cursive;
    color: var(--title-white);
    -webkit-text-stroke: 2px var(--ink);
    text-shadow: 4px 4px 0 var(--ink);
    transform: rotate(-6deg);
  }
  .title__bright {
    left: 36px; top: 162px;
    font: 104px "Anton", sans-serif;
    color: var(--title-red);
    -webkit-text-stroke: 2px var(--title-red-dark);
    text-shadow: 5px 5px 0 var(--ink);
    transform: rotate(-3deg);
  }
  .title__clinic {
    left: 38px; top: 266px;
    font: 104px "Oswald", sans-serif;
    font-weight: 700;
    color: var(--title-white);
    -webkit-text-stroke: 2px var(--title-cyan);
    text-shadow: 4px 4px 0 var(--title-cyan), 7px 7px 0 var(--ink);
    transform: scaleX(0.95) rotate(-3deg);
    transform-origin: left top;
    letter-spacing: 3px;
  }
  .title__growth {
    left: 70px; top: 378px;
    font: 60px "Anton", sans-serif;
    background: linear-gradient(180deg, var(--orange-top), var(--orange-bottom));
    -webkit-background-clip: text; background-clip: text;
    color: transparent;
    -webkit-text-stroke: 1.5px var(--title-red-dark);
    transform: skewX(-14deg) rotate(-4deg);
    filter: drop-shadow(3px 3px 0 var(--ink));
    letter-spacing: 2px;
  }
  .title__hour {
    left: 84px; top: 432px;
    font: 92px "Lobster", cursive;
    color: var(--title-white);
    -webkit-text-stroke: 2px var(--ink);
    text-shadow: 5px 5px 0 var(--ink);
    transform: rotate(-8deg);
  }
  .title__with {
    left: 318px; top: 498px;
    font: 40px "Lobster", cursive;
    color: var(--title-white);
    -webkit-text-stroke: 1.5px var(--ink);
    text-shadow: 3px 3px 0 var(--ink);
    transform: rotate(-8deg);
  }
  .host {
    position: absolute; left: 160px; top: 548px;
    width: 320px; margin: 0; text-align: center;
  }
  .host__name {
    display: block;
    font: 46px/1.1 "Archivo Black", sans-serif;
    background: linear-gradient(180deg, var(--name-top), var(--name-bottom));
    -webkit-background-clip: text; background-clip: text;
    color: transparent;
    -webkit-text-stroke: 1.5px var(--ink);
    filter: drop-shadow(3px 3px 0 var(--ink));
  }
</style>
</head>
<body>
<main class="sheet">

  <section class="cover-slot cover-slot--large">
    <div class="cover">
      <div class="cover__photo" role="img" aria-label="Photo of a stacked-stone clinic entrance"></div>
      <svg class="cover__layer" viewBox="0 0 711 711" aria-hidden="true">
        <defs>
          <linearGradient id="panelFillL" x1="0" y1="0" x2="1" y2="1">
            <stop offset="0" stop-color="#2f6d92"/>
            <stop offset=".5" stop-color="#5aa2c6"/>
            <stop offset="1" stop-color="#1d4660"/>
          </linearGradient>
        </defs>
        <polygon points="0,40 110,40 640,711 0,711" fill="url(#panelFillL)" stroke="#0d2636" stroke-width="4"/>
      </svg>
      <svg class="cover__layer" viewBox="0 0 711 711" role="img" aria-label="Photo of a vintage chrome studio microphone">
        <defs>
          <linearGradient id="micFillL" x1="0" y1="0" x2="1" y2="1">
            <stop offset="0" stop-color="#b9b09c"/>
            <stop offset="1" stop-color="#6d6558"/>
          </linearGradient>
        </defs>
        <polygon points="390,400 530,300 711,560 711,711 600,711" fill="url(#micFillL)"/>
      </svg>
      <div class="title">
        <p class="title__line title__the">The</p>
        <p class="title__line title__bright">BRIGHT</p>
        <p class="title__line title__clinic">CLINIC</p>
        <p class="title__line title__growth">GROWTH</p>
        <p class="title__line title__hour">Hour</p>
        <p class="title__line title__with">With</p>
        <p class="host"><span class="host__name">DR. DANA</span><span class="host__name">WHITLOW</span></p>
      </div>
    </div>
  </section>

  <section class="cover-slot cover-slot--medium">
    <div class="cover">
      <div class="cover__photo" role="img" aria-label="Photo of a stacked-stone clinic entrance"></div>
      <svg class="cover__layer" viewBox="0 0 711 711" aria-hidden="true">
        <defs>
          <linearGradient id="panelFillM" x1="0" y1="0" x2="1" y2="1">
            <stop offset="0" stop-color="#2f6d92"/>
            <stop offset=".5" stop-color="#5aa2c6"/>
            <stop offset="1" stop-color="#1d4660"/>
          </linearGradient>
        </defs>
        <polygon points="0,40 110,40 640,711 0,711" fill="url(#panelFillM)" stroke="#0d2636" stroke-width="4"/>
      </svg>
      <svg class="cover__layer" viewBox="0 0 711 711" role="img" aria-label="Photo of a vintage chrome studio microphone">
        <defs>
          <linearGradient id="micFillM" x1="0" y1="0" x2="1" y2="1">
            <stop offset="0" stop-color="#b9b09c"/>
            <stop offset="1" stop-color="#6d6558"/>
          </linearGradient>
        </defs>
        <polygon points="390,400 530,300 711,560 711,711 600,711" fill="url(#micFillM)"/>
      </svg>
      <div class="title">
        <p class="title__line title__the">The</p>
        <p class="title__line title__bright">BRIGHT</p>
        <p class="title__line title__clinic">CLINIC</p>
        <p class="title__line title__growth">GROWTH</p>
        <p class="title__line title__hour">Hour</p>
        <p class="title__line title__with">With</p>
        <p class="host"><span class="host__name">DR. DANA</span><span class="host__name">WHITLOW</span></p>
      </div>
    </div>
  </section>

  <section class="cover-slot cover-slot--small">
    <div class="cover">
      <div class="cover__photo" role="img" aria-label="Photo of a stacked-stone clinic entrance"></div>
      <svg class="cover__layer" viewBox="0 0 711 711" aria-hidden="true">
        <defs>
          <linearGradient id="panelFillS" x1="0" y1="0" x2="1" y2="1">
            <stop offset="0" stop-color="#2f6d92"/>
            <stop offset=".5" stop-color="#5aa2c6"/>
            <stop offset="1" stop-color="#1d4660"/>
          </linearGradient>
        </defs>
        <polygon points="0,40 110,40 640,711 0,711" fill="url(#panelFillS)" stroke="#0d2636" stroke-width="4"/>
      </svg>
      <svg class="cover__layer" viewBox="0 0 711 711" role="img" aria-label="Photo of a vintage chrome studio microphone">
        <defs>
          <linearGradient id="micFillS" x1="0" y1="0" x2="1" y2="1">
            <stop offset="0" stop-color="#b9b09c"/>
            <stop offset="1" stop-color="#6d6558"/>
          </linearGradient>
        </defs>
        <polygon points="390,400 530,300 711,560 711,711 600,711" fill="url(#micFillS)"/>
      </svg>
      <div class="title">
        <p class="title__line title__the">The</p>
        <p class="title__line title__bright">BRIGHT</p>
        <p class="title__line title__clinic">CLINIC</p>
        <p class="title__line title__growth">GROWTH</p>
        <p class="title__line title__hour">Hour</p>
        <p class="title__line title__with">With</p>
        <p class="host"><span class="host__name">DR. DANA</span><span class="host__name">WHITLOW</span></p>
      </div>
    </div>
  </section>

</main>
</body>
</html>
```